Real Estate Agent needs business card design

We have logo designed already, want to have business card designed. Very interested in those smaller size business card as they look very trendy. Business name is called VORENDA REALTY

```html
<!DOCTYPE html>
<html lang="en">
<head>
<meta charset="utf-8">
<title>Vorenda Realty – Round Business Card</title>
<link rel="stylesheet" href="https://fonts.googleapis.com/css2?family=Cormorant+SC:wght@500&family=Jost:wght@400&display=swap">
<style>
  :root {
    --page: #ffffff;
    --card-front: #ffffff;
    --gold: #c9a46c;
    --gold-light: #d5b182;
    --gold-deep: #c8a068;
    --ink: #222222;
    --edge: #e6e6e6;
  }
  html, body {
    margin: 0;
    padding: 0;
    width: 1200px;
    height: 840px;
    overflow: hidden;
    background: var(--page);
  }
  .canvas {
    position: relative;
    width: 1200px;
    height: 840px;
  }
  .card {
    position: absolute;
    top: 206px;
    width: 428px;
    height: 428px;
    border-radius: 50%;
    text-align: center;
    box-sizing: border-box;
  }
  .card--front {
    left: 160px;
    background: var(--card-front);
    border: 1px solid var(--edge);
    color: var(--ink);
    font-family: "Jost", sans-serif;
  }
  .card--back {
    left: 610px;
    background: linear-gradient(170deg, var(--gold-light) 0%, var(--gold-deep) 100%);
    color: #ffffff;
  }
  .abs {
    position: absolute;
    left: 0;
    right: 0;
    margin: 0;
  }
  .brand-dot {
    position: absolute;
    left: 50%;
    border-radius: 50%;
  }
  .card--front .brand-dot {
    top: 60px;
    width: 34px;
    height: 34px;
    margin-left: -17px;
    background: var(--gold);
  }
  .card--back .brand-dot {
    top: 136px;
    width: 70px;
    height: 70px;
    margin-left: -35px;
    background: #ffffff;
  }
  .brand-name {
    font-family: "Cormorant SC", serif;
    font-weight: 500;
    letter-spacing: 0.5px;
    line-height: 1;
  }
  .card--front .brand-name {
    top: 114px;
    font-size: 29px;
    color: var(--ink);
  }
  .card--back .brand-name {
    top: 228px;
    font-size: 46px;
    color: #ffffff;
  }
  .person-name {
    top: 173px;
    font-size: 21px;
    letter-spacing: 0.5px;
    color: var(--gold);
    line-height: 1;
  }
  .person-role {
    top: 199px;
    font-size: 15px;
    line-height: 1;
  }
  .divider {
    position: absolute;
    left: 50%;
    width: 21px;
    height: 2px;
    margin-left: -10px;
    background: var(--gold);
  }
  .divider--top { top: 229px; }
  .divider--bottom { top: 310px; }
  .contact {
    top: 244px;
    font-size: 13.5px;
    line-height: 18px;
  }
  .contact .label { color: var(--gold); }
  .address {
    top: 325px;
    font-size: 13.5px;
    line-height: 16px;
  }
  .web {
    top: 348px;
    font-family: "Jost", sans-serif;
    font-size: 14px;
    color: #ffffff;
  }
</style>
</head>
<body>
<main class="canvas">
  <section class="card card--front" aria-label="Card front">
    <span class="brand-dot"></span>
    <p class="abs brand-name">Vorenda Realty</p>
    <p class="abs person-name">Adrian Hale</p>
    <p class="abs person-role">Founder</p>
    <span class="divider divider--top"></span>
    <p class="abs contact">
      <span class="label">Cell:</span> (000)555-0188<br>
      <span class="label">Email:</span> info@adrianhale.com<br>
      <span class="label">Web:</span> www.vorendarealty.com
    </p>
    <span class="divider divider--bottom"></span>
    <p class="abs address">48 Linden Court<br>Brookfield, TN 37027</p>
  </section>

  <section class="card card--back" aria-label="Card back">
    <span class="brand-dot"></span>
    <p class="abs brand-name">Vorenda Realty</p>
    <p class="abs web">www.vorendarealty.com</p>
  </section>
</main>
</body>
</html>
```